Breast Cancer Car Donation Website Design

Please create a new one page website design.

Current site: http://www.giveautopinkribbon.org/

The NEW website address will be RidesforPinkHope.org

Use these sites for an idea of what I am looking for. I like these sites best: motorsforheroes.org and autosforservice.org

Coding

Coded - Design and coding required

Number of Pages Required

1 page

```html
<!DOCTYPE html>
<html lang="en">
<head>
<meta charset="utf-8">
<title>Rides for Pink Hope – Car &amp; Boat Donation</title>
<link href="https://fonts.googleapis.com/css2?family=Montserrat:wght@500;600;700&family=Lato:wght@400;700&display=swap" rel="stylesheet">
<style>
:root{
  --pink:#e0106e;
  --pink-soft:#ee6fa0;
  --pink-pale:#f7c9dc;
  --purple:#7b6fd6;
  --purple-dark:#4d3fb0;
  --ink:#555;
  --ink-dark:#333;
  --line:#d6d6d6;
  --grey-bg:#f3f3f3;
  --white:#fff;
}
*{box-sizing:border-box;margin:0;padding:0}
html,body{width:1200px;height:2397px;overflow:hidden}
body{position:relative;background:var(--white);font-family:'Lato',sans-serif;color:var(--ink)}
.abs{position:absolute}

/* header */
.site-header{left:0;top:0;width:1200px;height:145px;background:linear-gradient(90deg,#fbf3f6,#f6d3e2 45%,#fbeef3)}
.brand-mark{left:80px;top:14px;width:150px;height:120px;display:flex;align-items:center;gap:10px}
.brand-mark .dot{width:22px;height:22px;border-radius:50%;background:var(--pink);flex:none}
.brand-mark span{font-family:'Montserrat',sans-serif;font-weight:700;font-size:17px;line-height:1.15;color:var(--pink)}
.partner-name{left:935px;top:28px;width:190px;height:95px;display:flex;align-items:center;gap:10px}
.partner-name .sq{width:24px;height:24px;background:var(--purple);flex:none}
.partner-name span{font-family:'Montserrat',sans-serif;font-weight:600;font-size:19px;line-height:1.2;color:var(--ink-dark)}

.main-nav{left:0;top:145px;width:1200px;height:53px;background:var(--pink)}
.main-nav a{position:absolute;top:17px;font-family:'Montserrat',sans-serif;font-weight:500;font-size:16px;color:var(--white);text-decoration:none}

/* hero */
.hero-photo{left:0;top:198px;width:1200px;height:552px;background:linear-gradient(100deg,#f6c6d8 0%,#f1a9c6 35%,#f9d9e6 60%,#f2f2f4 100%)}
.donate-tab{left:665px;top:141px;width:458px;height:60px;background:var(--purple);color:var(--white);font-family:'Montserrat',sans-serif;font-weight:600;font-size:24px;letter-spacing:.5px;display:flex;align-items:center;justify-content:center}
.donate-tab::before,.donate-tab::after{content:"";position:absolute;bottom:-12px;border-top:12px solid var(--purple-dark)}
.donate-tab::before{left:0;border-left:14px solid transparent}
.donate-tab::after{right:0;border-right:14px solid transparent}
.donate-form{left:687px;top:201px;width:414px;height:549px;background:rgba(255,255,255,.85)}
.form-title{position:absolute;left:0;top:28px;width:414px;text-align:center;font-family:'Montserrat',sans-serif;font-weight:600;font-size:24px;line-height:37px;color:var(--pink)}
.field{position:absolute;left:24px;width:365px;height:37px;border:1px solid var(--line);background:var(--white);font-size:15px;color:#999;padding:9px 12px}
.field.half{width:177px}
.field.half::after{content:"";position:absolute;right:0;top:0;width:36px;height:35px;border-left:1px solid var(--line);background:linear-gradient(45deg,transparent 46%,#aaa 46%,#aaa 54%,transparent 54%) 9px 12px/9px 9px no-repeat,linear-gradient(-45deg,transparent 46%,#aaa 46%,#aaa 54%,transparent 54%) 17px 12px/9px 9px no-repeat}
.btn-donate{position:absolute;left:24px;top:441px;width:176px;height:39px;background:var(--purple);color:var(--white);font-family:'Montserrat',sans-serif;font-weight:600;font-size:17px;display:flex;align-items:center;justify-content:center}
.car-photo{left:688px;top:490px;width:512px;height:215px;background:linear-gradient(180deg,rgba(120,125,135,.0),rgba(110,115,125,.45));border-radius:60px 40px 10px 10px}

/* welcome */
.welcome-title{left:0;top:795px;width:1200px;text-align:center;font-family:'Montserrat',sans-serif;font-weight:700;font-size:42px;color:var(--pink)}
.welcome-text{left:150px;top:854px;width:900px;text-align:center;font-size:15px;line-height:25.5px;color:var(--ink)}
.feature-line{top:997px;height:0;border-top:2px dotted #ccc;width:176px}
.feature-icon{width:74px;height:74px;border:1.5px solid #ccc;border-radius:50%;background:var(--white);display:flex;align-items:center;justify-content:center}
.feature-label{width:220px;text-align:center;font-size:16px;line-height:27px;color:var(--ink)}

/* about */
.about-title{left:80px;top:1190px;font-family:'Montserrat',sans-serif;font-weight:700;font-size:43px;color:var(--pink)}
.about-text{left:80px;top:1257px;width:510px;font-size:15.5px;line-height:25.5px;color:var(--ink)}
.about-text p+p{margin-top:7px}
.btn-know{left:77px;top:1432px;width:187px;height:46px;background:var(--pink);color:var(--white);font-family:'Montserrat',sans-serif;font-weight:600;font-size:20px;display:flex;align-items:center;justify-content:center;border-radius:3px}
.screening-card{left:705px;top:1167px;width:417px;height:343px;background:linear-gradient(90deg,#eeeeee 0%,#f4a7c7 45%,#ee6fa0 100%);overflow:hidden}
.screening-head{position:absolute;left:0;top:0;width:417px;height:72px}
.screening-head span{position:absolute;left:0;top:16px;width:417px;text-align:center;font-family:'Montserrat',sans-serif;font-weight:600;font-size:30px;color:var(--white)}
.screening-copy{position:absolute;right:28px;top:201px;text-align:right;font-family:'Montserrat',sans-serif;font-weight:500;font-size:19px;line-height:29px;color:var(--white)}
.screening-dot{position:absolute;left:283px;top:102px;width:72px;height:72px;border-radius:50%;background:var(--white)}

/* faq */
.faq-section{left:0;top:1595px;width:1200px;height:510px;background:var(--grey-bg)}
.faq-title{left:0;top:1641px;width:1200px;text-align:center;font-family:'Montserrat',sans-serif;font-weight:700;font-size:41px;color:var(--pink)}
.faq-art{left:120px;top:1718px;width:272px;height:335px;background:linear-gradient(180deg,#ececec,#e3e3e3);border-radius:40px}
.faq-list{left:471px;top:1718px;width:603px}
.faq-item{position:relative;border-bottom:1px solid var(--line);padding:8px 0 10px 56px}
.faq-item .q{font-size:17px;color:var(--ink-dark);line-height:24px}
.faq-item .a{font-size:14.5px;line-height:24px;color:var(--ink);margin-top:4px;max-width:515px}
.faq-item svg{position:absolute;left:13px;top:12px}
.faq-item.open{padding-bottom:13px}
.faq-item.closed{height:47px}

/* footer */
.site-footer{left:0;top:2105px;width:1200px;height:292px;background:linear-gradient(90deg,#ee7aa6,#ec6a9d 50%,#ef7fa9)}
.call-label{left:0;top:2153px;width:1200px;text-align:center;font-family:'Montserrat',sans-serif;font-weight:600;font-size:24px;letter-spacing:.5px;color:var(--white)}
.call-number{left:0;top:2196px;width:1200px;display:flex;justify-content:center;align-items:center;gap:22px;font-family:'Montserrat',sans-serif;font-weight:600;font-size:42px;color:var(--white)}
.footer-rule{left:77px;top:2282px;width:1046px;height:1px;background:rgba(255,255,255,.8)}
.footer-links{left:0;top:2302px;width:1200px;text-align:center;font-size:15px;color:var(--white)}
.footer-links a{color:var(--white);text-decoration:none;margin:0 6px}
.copyright{left:0;top:2344px;width:1200px;text-align:center;font-size:15px;color:var(--white)}
</style>
</head>
<body>

<header class="abs site-header"></header>
<div class="abs brand-mark"><i class="dot"></i><span>Rides for<br>Pink Hope</span></div>
<div class="abs partner-name"><i class="sq"></i><span>Rosewell<br>Care Fund</span></div>

<div class="abs hero-photo" role="img" aria-label="Photo of three smiling women in pink shirts hugging, on a soft pink floral background"></div>
<div class="abs car-photo" role="img" aria-label="Photo of a grey sedan car"></div>

<nav class="abs main-nav">
  <a href="#" style="left:80px">HOME</a>
  <a href="#" style="left:176px">ABOUT</a>
  <a href="#" style="left:276px">FAQ</a>
  <a href="#" style="left:358px">CONTACT</a>
</nav>

<form class="abs donate-form">
  <div class="form-title">Running or not<br>No Emission Test Required</div>
  <div class="field" style="top:115px">First Name</div>
  <div class="field" style="top:161px">Last Name</div>
  <div class="field" style="top:207px">Daytime Phone</div>
  <div class="field" style="top:252px">Email</div>
  <div class="field" style="top:298px">Zip Code</div>
  <div class="field half" style="top:344px">Choose Year</div>
  <div class="field half" style="top:344px;left:212px">Choose Make</div>
  <div class="field" style="top:390px">Vehicle Model</div>
  <div class="btn-donate">DONATE NOW</div>
</form>
<div class="abs donate-tab">DONATE A CAR OR BOAT NOW</div>

<h1 class="abs welcome-title">Welcome Visitor!</h1>
<p class="abs welcome-text">Your car or boat donation helps support those stricken by breast cancer &amp; their families, and supports programs for screening, prevention, treatment and patient well being. Our operators are standing by 24 hours a day, 7 days a week to answer your questions and get your car or boat donation picked up quickly!</p>

<div class="abs feature-line" style="left:358px"></div>
<div class="abs feature-line" style="left:660px"></div>

<div class="abs feature-icon" style="left:262px;top:962px">
  <svg width="40" height="40" viewBox="0 0 40 40" fill="none" stroke="#444" stroke-width="2"><path d="M33 20a13 13 0 1 1-4-9.4"/><path d="M30 5v6h-6"/><text x="20" y="25" text-anchor="middle" font-family="Montserrat,sans-serif" font-size="12" font-weight="700" fill="#444" stroke="none">24</text></svg>
</div>
<div class="abs feature-icon" style="left:562px;top:962px">
  <svg width="40" height="40" viewBox="0 0 40 40" fill="none" stroke="#444" stroke-width="2"><rect x="8" y="16" width="24" height="16"/><path d="M12 22h10M12 27h14"/><path d="M16 16l4-10 4 10"/></svg>
</div>
<div class="abs feature-icon" style="left:863px;top:962px">
  <svg width="40" height="40" viewBox="0 0 40 40" fill="#444"><path d="M6 26l3-8c1-2 2-3 4-3h14c2 0 3 1 4 3l3 8v6H6z"/><circle cx="12" cy="32" r="3" fill="#fff" stroke="#444" stroke-width="2"/><circle cx="28" cy="32" r="3" fill="#fff" stroke="#444" stroke-width="2"/><path d="M18 6l4 4-4 4" fill="none" stroke="#444" stroke-width="2"/></svg>
</div>
<div class="abs feature-label" style="left:189px;top:1047px">Fast Free Pickup - 24hr<br>Response</div>
<div class="abs feature-label" style="left:489px;top:1047px">Tax Deduction - Easy<br>To Do!</div>
<div class="abs feature-label" style="left:790px;top:1047px">Running or not - No<br>Emission Test Required</div>

<h2 class="abs about-title">About us</h2>
<div class="abs about-text">
  <p>The Rosewell Care Fund is committed to making a positive difference in the lives of those afflicted with breast cancer as well as those families affected by breast cancer.</p>
  <p>The Rosewell Care Fund financially supports a variety of programs dedicated to breast cancer screening and prevention, treatment and patient health and well-being.</p>
</div>
<a class="abs btn-know">KNOW MORE</a>

<div class="abs screening-card" role="img" aria-label="Photo of a woman in a white tank top wearing a pink ribbon pin">
  <svg class="screening-head" width="417" height="72" viewBox="0 0 417 72"><path d="M0 0H417V72C300 52 140 58 0 72Z" fill="#7b6fd6"/></svg>
  <div class="screening-head"><span>FREE SCREANING</span></div>
  <div class="screening-dot"></div>
  <div class="screening-copy">For YOU!<br>For a Friend<br>For Someone in<br>your Family.</div>
</div>

<section class="abs faq-section"></section>
<h2 class="abs faq-title">FAQs</h2>
<div class="abs faq-art" role="img" aria-label="Line illustration of a female torso with a pink ribbon"></div>
<div class="abs faq-list">
  <div class="faq-item open">
    <svg width="20" height="20" viewBox="0 0 20 20" fill="none" stroke="#444" stroke-width="1.5"><circle cx="10" cy="10" r="8.5"/><path d="M5.5 10h9"/></svg>
    <div class="q">Lorem Ipsum is simply dummy text of the printing and typeset?</div>
    <div class="a">Lorem Ipsum is simply dummy text of the printing and typesetting industry. Lorem Ipsum has been the industry's standard dummy text ever since the 1500s, when an unknown printer took a galley of type and scrambled.</div>
  </div>
  <div class="faq-item closed">
    <svg width="20" height="20" viewBox="0 0 20 20" fill="none" stroke="#444" stroke-width="1.5"><circle cx="10" cy="10" r="8.5"/><path d="M5.5 10h9M10 5.5v9"/></svg>
    <div class="q">Lorem Ipsum is simply dummy text of the printing?</div>
  </div>
  <div class="faq-item closed">
    <svg width="20" height="20" viewBox="0 0 20 20" fill="none" stroke="#444" stroke-width="1.5"><circle cx="10" cy="10" r="8.5"/><path d="M5.5 10h9M10 5.5v9"/></svg>
    <div class="q">Lorem Ipsum is simply dummy text of the printing?</div>
  </div>
  <div class="faq-item closed">
    <svg width="20" height="20" viewBox="0 0 20 20" fill="none" stroke="#444" stroke-width="1.5"><circle cx="10" cy="10" r="8.5"/><path d="M5.5 10h9M10 5.5v9"/></svg>
    <div class="q">Lorem Ipsum is simply dummy text of the printing?</div>
  </div>
  <div class="faq-item closed">
    <svg width="20" height="20" viewBox="0 0 20 20" fill="none" stroke="#444" stroke-width="1.5"><circle cx="10" cy="10" r="8.5"/><path d="M5.5 10h9M10 5.5v9"/></svg>
    <div class="q">Lorem Ipsum is simply dummy text of the printing?</div>
  </div>
</div>

<footer class="abs site-footer"></footer>
<div class="abs call-label">CALL TODAY TO DONATE</div>
<div class="abs call-number">
  <svg width="40" height="40" viewBox="0 0 24 24" fill="#fff"><path d="M6.6 10.8a15.1 15.1 0 0 0 6.6 6.6l2.2-2.2c.3-.3.7-.4 1-.2 1.1.4 2.3.6 3.6.6.6 0 1 .4 1 1V20c0 .6-.4 1-1 1A17 17 0 0 1 3 4c0-.6.4-1 1-1h3.5c.6 0 1 .4 1 1 0 1.3.2 2.5.6 3.6.1.3 0 .7-.2 1z"/></svg>
  <span>888-555-0147</span>
</div>
<div class="abs footer-rule"></div>
<div class="abs footer-links"><a href="#">Home</a>|<a href="#">About</a>|<a href="#">FAQ</a>|<a href="#">Contact</a></div>
<div class="abs copyright">©Rides for Pink Hope- 2018. All Rights Reserved.</div>

</body>
</html>
```